Brightwave Learners Agency business cards

Australian company about to start offering its services. We recruit international students to come to study English, vocational education and postgraduate courses in Australia. We help them find the institution and select the right city they want to come to Australia. We are a young, online oriented and supportive agency. Our clients are between 18 and 35 years old, mainly University students, young professionals or people with work experience. We provide much more information that any other agency offer. We administrate a Facebook group with more than 11.000 members that daily ask questions about general information when coming to Australia, while they are here and even after they leave the country

Target Market(s)

International students from South America, Central America and Europe

Industry/Entity Type

Student

Contact Information for Business Card

Tomas Velorin
Managing Director
tomas@kelvona.com.au
www.kelvrona.com.au
+61 497285064
Melbourne, Australia

Font styles to use
Serif
Sans Serif

Colors

Designer to choose colors to be used in the design.

Requirements
Must have
• Horizontal design
• Standard business card size and shape. If font uses green or yellow colours, they will have to match the ones from the logo
Nice to have
• UPDATE: Use the contents of the green image to design one of the card sides. Use our logo in the background of that side as watermark.
• Passport image, or immigration stamps. A picture of the Yarra River (from Melbourne) would be cool as well.
Should not have
• Non-standard business card size and shape
• Not black as the background colour of any sides as we are not a VIP agency or a hight class service. We are orientes to young people and they like colours, pictures, something attractive.
• Vertical design
• NO YELLOW or BLACK AS THE BACKGROUND COLOUR OF ANY SIDE OF THE BIZ CARD

```html
<!DOCTYPE html>
<html lang="en">
<head>
<meta charset="utf-8">
<title>Brightwave Learners Agency – Business Cards</title>
<link rel="stylesheet" href="https://fonts.googleapis.com/css2?family=PT+Sans:wght@400;700&display=swap">
<style>
  :root {
    --stage: #d9d6d2;
    --card-green: #17633a;
    --card-green-deep: #0f4a2a;
    --card-glow: #23804c;
    --brand-yellow: #f2c418;
    --brand-green-dark: #0b3a20;
    --text-white: #ffffff;
  }
  * { margin: 0; padding: 0; box-sizing: border-box; }
  html, body {
    width: 1200px; height: 843px; overflow: hidden;
    background: var(--stage);
    font-family: "PT Sans", "Myriad Pro", Arial, sans-serif;
  }
  .canvas {
    position: relative; width: 1200px; height: 843px;
    display: flex; align-items: center; justify-content: center; gap: 40px;
  }
  .card {
    position: relative; width: 520px; height: 297px;
    overflow: hidden;
    box-shadow: 0 6px 18px rgba(0,0,0,.25);
  }

  /* Contact side */
  .card--contact {
    background: linear-gradient(160deg, var(--card-glow) 0%, var(--card-green) 45%, var(--card-green-deep) 100%);
  }
  .band {
    position: absolute; left: 0; right: 0; height: 11px;
    background: var(--brand-yellow);
  }
  .band--top { top: 14px; }
  .band--bottom { bottom: 14px; }
  .contact {
    position: absolute; left: 130px; width: 260px; top: 72px;
    text-align: center;
    color: var(--text-white); font-size: 14px; line-height: 1.3;
  }
  .contact__name { color: var(--brand-yellow); font-weight: 700; font-size: 19px; line-height: 1.15; }
  .contact__role { font-size: 13px; }
  .contact__city { margin-top: 22px; }
  .contact__lines { margin-top: 22px; }
  .contact__lines p { line-height: 1.32; }

  /* Brand side */
  .card--brand {
    background: radial-gradient(ellipse at 50% 42%, var(--card-glow) 0%, var(--card-green) 45%, var(--card-green-deep) 100%);
  }
  .brand {
    position: absolute; left: 0; right: 0; top: 100px;
    text-align: center; color: var(--brand-yellow);
    font-weight: 700; font-size: 40px; line-height: 1;
  }
  .tagline {
    position: absolute; left: 0; right: 0; top: 196px;
    text-align: center; color: var(--brand-yellow);
    font-weight: 700; font-size: 12px; letter-spacing: .3px;
  }
  .tab {
    position: absolute; width: 26px; height: 34px;
    background: var(--brand-yellow);
  }
  .tab--left { left: 0; top: 178px; border-left: 4px solid var(--brand-green-dark); }
  .tab--right { right: 0; top: 18px; border-right: 4px solid var(--brand-green-dark); }
</style>
</head>
<body>
  <main class="canvas">
    <section class="card card--contact" aria-label="Business card, contact side">
      <div class="band band--top"></div>
      <div class="contact">
        <p class="contact__name">Tomas Velorin</p>
        <p class="contact__role">Managing Director</p>
        <p class="contact__city">Melbourne, Australia</p>
        <div class="contact__lines">
          <p>+61 497285064</p>
          <p>tomas@kelvona.com.au</p>
          <p>www.kelvrona.com.au</p>
        </div>
      </div>
      <div class="band band--bottom"></div>
    </section>

    <section class="card card--brand" aria-label="Business card, brand side">
      <div class="tab tab--right"></div>
      <p class="brand">Brightwave</p>
      <p class="tagline">HACEMOS MÁS POR TI!</p>
      <div class="tab tab--left"></div>
    </section>
  </main>
</body>
</html>
```